" atendimento de pacientes de ambos os gêneros com uma ênfase em mulheres, oferecemos cirurgia plástica estética e reparadora . local de requinte e sofisticação "

```html
<!DOCTYPE html>
<html lang="pt-BR">
<head>
<meta charset="utf-8">
<title>Receituário de Controle Especial</title>
<link href="https://fonts.googleapis.com/css2?family=Open+Sans:wght@400;600&display=swap" rel="stylesheet">
<style>
  :root{
    --bg:#e4e6e9;
    --paper:#ffffff;
    --ink:#1c1c1c;
    --band:#0d0d0d;
    --gold:#c9a35a;
    --gold-light:#e9d3a0;
    --line:#6e6e6e;
    --label:#555;
    --haze:#eef0f2;
  }
  *{box-sizing:border-box;margin:0;padding:0}
  html,body{width:1200px;height:1200px;overflow:hidden}
  body{background:var(--bg);font-family:"Open Sans",Arial,sans-serif;color:var(--ink);position:relative}
  .sheet{position:absolute;left:200px;top:35px;width:800px;height:1130px;background:var(--paper);box-shadow:0 12px 40px rgba(0,0,0,.18);overflow:hidden}
  .band-top,.band-bottom{position:absolute;left:0;width:100%}
  .band-top{top:0;height:110px}
  .band-bottom{bottom:0;height:110px}
  .form-title{position:absolute;top:22px;width:100%;text-align:center;color:#fff;font-size:20px;font-weight:400;letter-spacing:.3px}
  .issuer{position:absolute;left:70px;top:140px;width:420px;height:160px;border:1.5px solid var(--ink);border-radius:14px}
  .issuer-label{position:absolute;top:-1px;left:50%;transform:translateX(-50%);font-size:10px;color:var(--label);background:var(--paper);padding:0 10px;border:1px solid var(--line);border-top:none;border-radius:0 0 6px 6px;white-space:nowrap}
  .brand{position:absolute;left:28px;top:55px;display:flex;align-items:center;gap:8px}
  .brand-mark{width:12px;height:12px;border-radius:50%;background:var(--gold)}
  .brand-name{font-size:30px;color:var(--gold);font-weight:400;letter-spacing:1px}
  .brand-sub{position:absolute;left:48px;top:96px;font-size:9px;letter-spacing:2px;color:var(--gold)}
  .doctor{position:absolute;left:230px;top:58px;font-size:13px;line-height:1.3}
  .copies{position:absolute;right:80px;top:200px;font-size:11px;font-weight:600;text-align:right;line-height:1.4}
  .field{position:absolute;left:70px;width:630px;font-size:15px;color:#444;display:flex;align-items:flex-end;gap:12px}
  .field .rule{flex:1;border-bottom:1px solid var(--line);height:14px}
  .field.patient{top:322px}
  .field.address{top:352px}
  .prescription{position:absolute;left:70px;top:385px;font-size:22px;color:#333}
  .portrait-area{position:absolute;left:0;top:430px;width:360px;height:380px;background:radial-gradient(ellipse at 40% 50%,var(--haze),rgba(255,255,255,0) 70%)}
  .signature{position:absolute;left:200px;top:820px;width:240px;border-top:1px solid var(--line);text-align:center;font-size:9px;color:var(--label);padding-top:3px}
  .buyer{position:absolute;left:70px;top:860px;width:300px;height:150px;border:1.5px solid var(--ink);border-radius:12px}
  .box-title{position:absolute;top:-1px;left:50%;transform:translateX(-50%);font-size:11px;background:var(--paper);padding:0 8px;border:1px solid var(--line);border-top:none;border-radius:0 0 6px 6px;white-space:nowrap}
  .buyer-row{position:absolute;left:14px;right:14px;border-bottom:1px solid var(--line);font-size:8px;color:var(--label);display:flex;justify-content:space-between;padding-bottom:1px}
  .supplier{position:absolute;left:430px;top:885px;width:300px;height:120px;border:1.5px solid var(--ink);border-radius:12px}
  .supplier-sign{position:absolute;left:18px;right:18px;bottom:18px;border-top:1px solid var(--line);font-size:8px;color:var(--label);display:flex;justify-content:space-between;padding-top:2px}
</style>
</head>
<body>
<main class="sheet">
  <svg class="band-top" viewBox="0 0 800 110" preserveAspectRatio="none" aria-hidden="true">
    <path d="M0 0H800V62Q400 90 0 62Z" fill="var(--band)"/>
    <path d="M0 66Q400 94 800 66" stroke="var(--gold)" stroke-width="2" fill="none"/>
  </svg>
  <h1 class="form-title">Receituário de Controle Especial</h1>

  <section class="issuer">
    <span class="issuer-label">Identificação do Emitente</span>
    <div class="brand"><span class="brand-mark"></span><span class="brand-name">AURÉLIA</span></div>
    <div class="brand-sub">CIRURGIA PLÁSTICA</div>
    <div class="doctor">Dra. Nome Completo<br>Especialidade<br>CRM. 000000</div>
  </section>
  <div class="copies">1ª VIA - PACIENTE<br>2ª VIA - EMITENTE</div>

  <div class="field patient"><span>Paciente</span><span class="rule"></span></div>
  <div class="field address"><span>Endereço</span><span class="rule"></span></div>
  <div class="prescription">Prescrição</div>

  <div class="portrait-area" role="img" aria-label="Ilustração suave em marca d'água de perfil feminino"></div>

  <div class="signature">Assinatura Médico</div>

  <section class="buyer">
    <span class="box-title">Identificação do Comprador</span>
    <div class="buyer-row" style="top:34px"><span>Nome</span></div>
    <div class="buyer-row" style="top:60px"><span>Identidade</span><span>Órgão Emissor</span></div>
    <div class="buyer-row" style="top:86px"><span>Endereço</span></div>
    <div class="buyer-row" style="top:112px"><span>Cidade</span><span>UF</span></div>
    <div class="buyer-row" style="top:132px;border:none"><span>Telefone</span></div>
  </section>

  <section class="supplier">
    <span class="box-title">Identificação do Fornecedor</span>
    <div class="supplier-sign"><span>Assinatura Fornecedor</span><span>/ &nbsp; /</span></div>
  </section>

  <svg class="band-bottom" viewBox="0 0 800 110" preserveAspectRatio="none" aria-hidden="true">
    <path d="M0 45Q400 20 800 45V110H0Z" fill="var(--band)"/>
    <path d="M0 40Q400 15 800 40" stroke="var(--gold)" stroke-width="2" fill="none"/>
    <path d="M0 34Q400 8 800 34" stroke="var(--gold-light)" stroke-width="1" fill="none"/>
  </svg>
</main>
</body>
</html>
```